Business Card Design Project

Small privately owned salon.

Industry/Entity Type

Business

Contact Information for Business Card

Hair salon.i would like my logo to be my name , Marisol Denby. Address and phone can go on the front or back. The back will be where I write their appt.
address-362 Thistledown lane York, Pa. 17488
Phone- 717-555-0148

```html
<!DOCTYPE html>
<html lang="en">
<head>
<meta charset="utf-8">
<title>Marisol Denby – Business Card</title>
<link href="https://fonts.googleapis.com/css2?family=Montserrat:wght@500;600&display=swap" rel="stylesheet">
<style>
  :root{
    --backdrop:#e9e6e4;
    --card-black:#1d1d1e;
    --card-black-soft:#262627;
    --salon-pink:#d21d6e;
    --salon-pink-deep:#b51560;
    --silver:#c9c9cb;
    --silver-band:#a9a9ab;
    --white:#ffffff;
  }
  *{margin:0;padding:0;box-sizing:border-box;}
  html,body{width:1200px;height:649px;overflow:hidden;background:var(--backdrop);}
  body{font-family:"Montserrat",Arial,sans-serif;position:relative;}

  .card{
    position:absolute;top:176px;width:520px;height:297px;
    background:radial-gradient(circle at 40% 35%,var(--card-black-soft),var(--card-black));
    box-shadow:0 10px 28px rgba(0,0,0,.22);
    overflow:hidden;
  }
  .card--back{left:50px;}
  .card--front{left:630px;}

  .brand-name{
    position:absolute;font-weight:600;font-size:38px;letter-spacing:.5px;white-space:nowrap;
  }
  .card--back .brand-name{left:0;right:0;top:98px;text-align:center;color:var(--silver);}
  .card--front .brand-name{left:34px;top:54px;font-size:34px;color:var(--salon-pink);}

  .social-row{
    position:absolute;left:0;right:0;top:240px;
    display:flex;align-items:center;justify-content:center;gap:6px;
  }
  .social-row .rule{width:62px;height:2px;background:var(--salon-pink);}
  .social-row .dot{width:24px;height:24px;border:2px solid var(--salon-pink);border-radius:50%;}

  .front-swoosh{position:absolute;inset:0;width:520px;height:297px;}

  .contact{
    position:absolute;right:40px;top:212px;text-align:right;color:var(--white);
    font-weight:500;font-size:15px;line-height:21px;
  }
  .contact .phone{margin-top:4px;display:flex;align-items:center;justify-content:flex-end;gap:6px;}
  .contact .phone svg{width:13px;height:13px;}
</style>
</head>
<body>

  <section class="card card--back" aria-label="Card back">
    <div class="brand-name">Marisol Denby</div>
    <div class="social-row">
      <span class="rule"></span>
      <span class="dot"></span><span class="dot"></span><span class="dot"></span><span class="dot"></span>
      <span class="rule"></span>
    </div>
  </section>

  <section class="card card--front" aria-label="Card front">
    <svg class="front-swoosh" viewBox="0 0 520 297" aria-hidden="true">
      <defs>
        <linearGradient id="pinkFill" x1="0" y1="1" x2="1" y2="0">
          <stop offset="0" stop-color="var(--salon-pink-deep)"/>
          <stop offset="1" stop-color="var(--salon-pink)"/>
        </linearGradient>
      </defs>
      <path d="M0 225 C140 240 300 190 400 120 C450 85 485 45 520 0 L520 297 L0 297 Z" fill="var(--silver-band)"/>
      <path d="M0 268 C170 262 330 215 420 140 C465 100 495 55 520 0 L520 297 L0 297 Z" fill="#111"/>
      <path d="M0 274 C175 268 335 222 425 146 C468 106 498 60 520 6 L520 297 L0 297 Z" fill="url(#pinkFill)"/>
    </svg>
    <div class="brand-name">Marisol Denby</div>
    <div class="contact">
      <div>362 Thistledown lane York</div>
      <div>Pa. 17488</div>
      <div class="phone">
        <svg viewBox="0 0 24 24" aria-hidden="true"><path fill="#fff" d="M6.6 10.8a15.1 15.1 0 0 0 6.6 6.6l2.2-2.2a1 1 0 0 1 1-.25 11.4 11.4 0 0 0 3.6.57 1 1 0 0 1 1 1V20a1 1 0 0 1-1 1A17 17 0 0 1 3 4a1 1 0 0 1 1-1h3.5a1 1 0 0 1 1 1c0 1.25.2 2.45.57 3.57a1 1 0 0 1-.25 1z"/></svg>
        <span>717-555-0148</span>
      </div>
    </div>
  </section>

</body>
</html>
```